Federal Contracting Capabilities Statement Re-Design

We're looking for alternate designs for the uploaded file. Here are the parameters:

- 1 page
- Layout (sections, order) needs to remain the same:
Summary
Core Competencies
Differentiators
Corporate Data
Past Performance
Workshop Capabilities

Please use content provided.

We have provided images to include, but high-quality, relevant stock photography can also be included. For additional resources, logo, images, content, etc.:

https://plumvestgroup.net/
https://www.linkedin.com/in/gordon-hale-plumvest/

```html
<!DOCTYPE html>
<html lang="en">
<head>
<meta charset="utf-8">
<title>Plumvest Group – Capabilities Statement</title>
<link href="https://fonts.googleapis.com/css2?family=Poppins:wght@400;600;700;800&display=swap" rel="stylesheet">
<style>
:root{
  --blue:#1d3a8f;
  --yellow:#fbc313;
  --yellow-light:#ffe27a;
  --ink:#222;
  --paper:#fff;
  --backdrop:#d9d9d9;
  --seal:#e4e8f2;
}
*{box-sizing:border-box;margin:0;padding:0}
html,body{width:1200px;height:1117px;overflow:hidden;background:var(--backdrop);font-family:'Poppins',sans-serif;color:var(--ink)}
.sheet-frame{position:absolute;left:180px;top:15px;width:840px;height:1086px;box-shadow:0 10px 30px rgba(0,0,0,.25)}
.sheet{position:absolute;left:0;top:0;width:1155px;height:1492px;background:var(--paper);transform:scale(.7273);transform-origin:0 0;overflow:hidden}
.abs{position:absolute}
.brand{left:48px;top:34px;display:flex;align-items:center;gap:14px}
.brand-dot{width:66px;height:66px;border-radius:50%;background:var(--yellow)}
.brand-name{font-weight:700;color:var(--blue);font-size:27px;line-height:1.05}
.photo{position:absolute}
.photo-team{left:0;top:125px;width:302px;height:218px;background:linear-gradient(135deg,#8b7a70,#4b4448 60%,#2e2a30)}
.photo-founder{left:310px;top:0;width:243px;height:343px;background:linear-gradient(180deg,#e8e4dc,#9cb8d8 55%,#7fa4cf)}
.top-band{left:553px;top:0;width:602px;height:143px;background:var(--blue)}
.top-stripe{left:553px;top:143px;width:602px;height:17px;background:var(--yellow)}
.photo-rack{left:598px;top:37px;width:512px;height:200px;background:var(--paper)}
.photo-hands{left:605px;top:45px;width:245px;height:188px;background:linear-gradient(135deg,#5d6e77,#2c3a42)}
.photo-speaker{left:856px;top:45px;width:246px;height:188px;background:linear-gradient(135deg,#c9c3b5,#5e5a52 60%,#2a2a2a)}
.section-head{position:absolute;height:48px}
.section-head .bar{position:absolute;left:20px;top:6px;right:0;height:36px;border-radius:0 18px 18px 0;background:linear-gradient(90deg,var(--yellow) 60%,var(--yellow-light) 88%,var(--yellow))}
.section-head .title{position:absolute;left:70px;top:9px;font-weight:800;font-size:20px;color:var(--blue);letter-spacing:.2px}
.section-head .icon{position:absolute;left:0;top:0;width:48px;height:48px;border-radius:50%;background:var(--blue);border:3px solid var(--paper);box-shadow:0 0 0 2px var(--blue);display:flex;align-items:center;justify-content:center}
.body-text{font-size:17px;line-height:22.6px}
.summary{left:95px;top:430px;width:462px}
.comp-photo{position:absolute;left:92px;width:134px;height:140px}
.comp-1{top:663px;background:linear-gradient(135deg,#5b4a42,#e9dede 55%,#f3eef0)}
.comp-2{top:816px;background:linear-gradient(135deg,#3d5a88,#c9c6c2 50%,#8d8a86)}
.comp-3{top:970px;background:linear-gradient(135deg,#d8d6d2,#2f3a44 60%,#1d2328)}
.comp-group{position:absolute;left:245px;width:320px}
.sub{font-weight:700;color:var(--blue);font-size:17px;line-height:24px}
.dot-list{list-style:none}
.dot-list li{position:relative;padding-left:23px;font-size:17px;line-height:22.6px}
.dot-list li::before{content:"";position:absolute;left:2px;top:6px;width:11px;height:11px;border-radius:50%;background:var(--blue)}
.tick-list{list-style:none}
.tick-list li{position:relative;padding-left:23px;font-size:17px;line-height:21px}
.tick-list li::before{content:"";position:absolute;left:2px;top:5px;width:10px;height:6px;border-left:2.5px solid var(--blue);border-bottom:2.5px solid var(--blue);transform:rotate(-45deg)}
.diff{left:95px;top:1198px;width:462px}
.diff li{margin-bottom:9px}
.strong-blue{font-weight:700;color:var(--blue)}
.corp{left:638px;top:326px;width:480px;font-size:17px;line-height:22.6px}
.lbl{font-weight:700;color:var(--blue)}
.naics{display:grid;grid-template-columns:85px 1fr}
.naics div{line-height:20px}
.badge{position:absolute}
.badge-round{left:972px;top:352px;width:52px;height:48px;border-radius:50%;border:3px solid #3d5ba8;background:#eef2fb}
.badge-rect{left:1038px;top:361px;width:62px;height:28px;background:#3b2b8f;border-radius:2px}
.seal{position:absolute;left:600px;width:62px;height:62px;border-radius:50%;background:var(--seal)}
.pp{position:absolute;left:675px;width:440px;font-size:17px;line-height:22.6px}
.workshop{left:640px;top:1080px;width:455px}
.foot-yellow{left:0;top:1446px;width:1155px;height:10px;background:var(--yellow)}
.foot-blue{left:0;top:1465px;width:1155px;height:27px;background:var(--blue)}
</style>
</head>
<body>
<div class="sheet-frame">
<div class="sheet">
  <div class="abs brand"><div class="brand-dot"></div><div class="brand-name">Plumvest<br>Group</div></div>
  <div class="photo photo-team" role="img" aria-label="Founder taking a group photo with a class of students"></div>
  <div class="photo photo-founder" role="img" aria-label="Portrait of the founder in a light blue company t-shirt"></div>
  <div class="abs top-band"></div>
  <div class="abs top-stripe"></div>
  <div class="abs photo-rack"></div>
  <div class="photo photo-hands" role="img" aria-label="Overhead view of a team joining hands over a meeting table"></div>
  <div class="photo photo-speaker" role="img" aria-label="Founder presenting in front of a projection screen"></div>

  <div class="section-head" style="left:57px;top:373px;width:496px">
    <div class="bar"></div><div class="title">SUMMARY</div>
    <div class="icon"><svg width="22" height="22" viewBox="0 0 22 22" fill="none" stroke="#fff" stroke-width="2"><rect x="4" y="2" width="13" height="18" rx="1"/><path d="M7 7h7M7 11h7M7 15h4"/></svg></div>
  </div>
  <p class="abs body-text summary">Plumvest Group is an independent consulting, training and development firm focused on increasing the effectiveness of federal government teams and individuals in the areas of acquisition, contracting, leadership, administrative and program management. We deliver value through experiential learning and demonstrated expertise.</p>

  <div class="section-head" style="left:57px;top:604px;width:496px">
    <div class="bar"></div><div class="title">CORE COMPETENCIES</div>
    <div class="icon"><svg width="22" height="22" viewBox="0 0 22 22" fill="none" stroke="#fff" stroke-width="2"><circle cx="9" cy="6" r="3.5"/><path d="M3 20v-5a5 5 0 0 1 10 0"/><circle cx="16" cy="16" r="4"/><path d="M14 16l1.5 1.5L18 15"/></svg></div>
  </div>
  <div class="comp-photo comp-1" role="img" aria-label="Consultant writing a plan on a whiteboard"></div>
  <div class="comp-photo comp-2" role="img" aria-label="Hands reviewing charts on a tablet"></div>
  <div class="comp-photo comp-3" role="img" aria-label="Trainer leading a workshop session"></div>
  <div class="comp-group" style="top:661px">
    <div class="sub">Acquisition / Procurement Services</div>
    <ul class="dot-list"><li>Acquisition Planning</li><li>Contract Management</li><li>Project Management</li><li>Strategic Planning &amp; Execution</li><li>Federal Acquisition Training</li><li>Best-In-Class Solution</li></ul>
  </div>
  <div class="comp-group" style="top:843px">
    <div class="sub">Development</div>
    <ul class="dot-list"><li>Data Analysis</li><li>Predictive Data Modeling</li><li>Efficiency Modeling</li><li>Effectiveness Modeling</li></ul>
  </div>
  <div class="comp-group" style="top:993px">
    <div class="sub">Training &amp; Development Services</div>
    <ul class="dot-list"><li>Leadership Development</li><li>High Performance Teambuilding</li><li>Personnel Development</li><li>Executive Coaching</li></ul>
  </div>

  <div class="section-head" style="left:57px;top:1131px;width:496px">
    <div class="bar"></div><div class="title">DIFFERENTIATIORS</div>
    <div class="icon"><svg width="22" height="22" viewBox="0 0 22 22" fill="none" stroke="#fff" stroke-width="2"><circle cx="11" cy="8" r="6"/><path d="M7 13l-2 7 4-2 2 3M15 13l2 7-4-2-2 3"/></svg></div>
  </div>
  <ul class="abs tick-list diff">
    <li>26 Years of experience in procurement, acquisition and program management</li>
    <li>Former Head of Contracting Activity</li>
    <li><span class="strong-blue">Senior Executive Service (SES)</span></li>
    <li>Trusted acquisition professional charged with training and development of generations of newly hired contracting interns regarding acquisition methodology, and contracting strategy, processes and techniques</li>
  </ul>

  <div class="section-head" style="left:602px;top:265px;width:498px">
    <div class="bar"></div><div class="title">CORPORATE DATA</div>
    <div class="icon"><svg width="22" height="22" viewBox="0 0 22 22" fill="none" stroke="#fff" stroke-width="2"><rect x="3" y="3" width="16" height="12" rx="1"/><path d="M7 12V9M11 12V7M15 12v-2M11 15v4"/></svg></div>
  </div>
  <div class="abs corp">
    <div><span class="lbl">CAGE:</span> 7QX42 | <span class="lbl">CAGE:</span> K8R3TPLW5HB2 | <span class="lbl">Work Area:</span> USA</div>
    <div><span class="lbl">Gov. Bus. POC:</span> Gordon Hale</div>
    <div><span class="lbl" style="display:inline-block;width:85px">Phone:</span>(555) 240-7318</div>
    <div><span class="lbl" style="display:inline-block;width:85px">E-Mail:</span>gordon@plumvestgroup.net</div>
    <div><span class="lbl">Address:</span> 418 Harbor Crest Lane - Norfolk, VA 23510</div>
    <div><span class="lbl">Socio-Economic Status:</span> SDVOSB, MBE, SWaM</div>
    <div class="naics">
      <div class="lbl">NAICS:</div><div>541611(P) - Admin. Mgmt. &amp; General Mgmt. Consulting</div>
      <div></div><div style="margin-top:10px">611430 - Professional Mgmt. Development Training</div>
    </div>
  </div>
  <div class="badge badge-round"></div>
  <div class="badge badge-rect"></div>

  <div class="section-head" style="left:602px;top:579px;width:498px">
    <div class="bar"></div><div class="title">PAST PERFORMANCE</div>
    <div class="icon"><svg width="22" height="22" viewBox="0 0 22 22" fill="none" stroke="#fff" stroke-width="2"><path d="M4 19v-4M8 19v-7M12 19v-9M16 19V8M3 10l6-4 4 2 6-5"/></svg></div>
  </div>
  <div class="seal" style="top:645px"></div>
  <div class="pp" style="top:641px">
    <div class="lbl">Past Performance</div>
    <div>Department of Civic Readiness</div>
    <div>Central HQ Service</div>
    <div><span class="lbl">Date(s):</span> 2020-2021 | <span class="lbl">Value:</span> $460,000+</div>
    <div><span class="lbl">Details:</span> Contracting Acceleration Program</div>
    <div><span class="lbl">Award Registry:</span> Central Headquarters Service</div>
    <div><span class="lbl">P-Card Contracts:</span> Over $82k from 2020 - Current</div>
  </div>
  <div class="seal" style="top:835px"></div>
  <div class="pp" style="top:832px">
    <div class="lbl">Department of Public Safety</div>
    <div class="lbl">National Harbor Patrol</div>
    <div><span class="lbl">Date(s):</span> 2019 | <span class="lbl">Value:</span> $7.5k+</div>
    <div><span class="lbl">Details:</span> Emerging Leader Training<br>(NHP Civilians)</div>
    <div><span class="lbl">Award Registry:</span> National Harbor Patrol</div>
    <div><span class="lbl">P-Card Contracts:</span> Over $82k from 2020 - Current</div>
  </div>

  <div class="section-head" style="left:602px;top:1016px;width:498px">
    <div class="bar"></div><div class="title">WORKSHOP CAPABILITIES</div>
    <div class="icon"><svg width="22" height="22" viewBox="0 0 22 22" fill="none" stroke="#fff" stroke-width="2"><circle cx="11" cy="11" r="3"/><circle cx="11" cy="11" r="7.5" stroke-dasharray="3 2.9"/></svg></div>
  </div>
  <ul class="abs tick-list workshop">
    <li>Contracts Management and Procurement Execution</li>
    <li>Leadership and Workforce Development</li>
    <li>Soft Skill Development and Coaching</li>
    <li>Transformational Leadership</li>
    <li>DISC Workplace Behavioral Assessments and Coaching</li>
    <li>Federal Acquisition Regulations System &amp; Guiding Principles</li>
    <li>Market Research Strategies</li>
    <li>Purchase Requests (PR) Processes</li>
    <li>Performance-Based Requirements Definition<br><span class="strong-blue">• SOW vs. SOO vs. PWS</span></li>
    <li>Independent Government Cost Estimates (IGCE)</li>
    <li>High Performance Teams</li>
    <li>COR Training and Refreshers</li>
  </ul>

  <div class="abs foot-yellow"></div>
  <div class="abs foot-blue"></div>
</div>
</div>
</body>
</html>
```